Industrial Company Website

We need a Website to highlight 5 different Brands we distribute.

We are Dealers for the following products

1)Velorin Tube a Div of Darvell Ostrick ( HDPE Pipes and Fittings )
Velorin Tube is the largest provider of polyethylene pipe (poly pipe) - HDPE pressure pipe and fittings in North America
Inquire page for web user to request pricing.

2) Brantock Weldline Mfg . ( HDPE Fusion Equipment )'
We like to have a system we are able to list top 25 items with part numbers and cost
that a web user is able to select and add to cart and email a order via the web.

3) Olvane Power ( Gate , Check and Globe Valves )
Sub Category Brands , Tessmark , Varilok , and Hollister Valves

4) Fertani North America Valves
http://www.fertaninorthamerica.example/ita/home.pag

5) Corlett Strainers, Inc. - A worldwide manufacturer of heavy-duty air, lube, fuel, coolant, transmission, and hydraulic filtration products
Within this Tab we like to web user to lookup filters from
http://catalog.corlettstrainer.example/ and able to create a inquire
for our company to send a quote .

6) Hargrove-Tamsin Uniforms
http://www.tamsinwear.example/
http://www.gardlyne.example/fireservice/

http://www.pelstrideboots.example/ (Safety Shoes)

Also we like a Tab for Company Profile , and contact information

We have authorization from all companies listed about to use their logo
under our dealership agreements.
Updates

Hello All ,

Please do not use the Tarvix Oil & Gas Logo.

Please Only use the Logo with the Logo with the M and the Flame and Oil Drop

Rex                                   

Target Market(s)

Target Markets ,: International distributor of pipe, valves, fittings and more
serving the Caribbean and South America .

Target Clients : Oil and Gas , Power Plants and Mining Companies

The Web Address will be www.tarvixsupply.example

Industry/Entity Type

It Company

Requirements
Must have
• Note : This Project will possibly lead to the next stage.
Coded and HTML proof of concept to load live.
I will give the winner first chance to Quote me the completion

Note the Goal is to have a E-Comm. Site , but since we are in Wholesale
and not retail . The E-Cart will no take payment but create an inquire and then send me to my email for processing
Nice to have
• I just had a Logo created by a designer on Graphic hive. I will need to share the logo design for your submission

```html
<!DOCTYPE html>
<html lang="en">
<head>
<meta charset="utf-8">
<title>Tarvix Oil &amp; Gas</title>
<link href="https://fonts.googleapis.com/css2?family=PT+Sans:wght@400;700&display=swap" rel="stylesheet">
<style>
:root{
  --gold:#a3962a;
  --text:#555;
  --heading:#555;
  --page:#f1f1f1;
  --white:#fff;
  --line:#dcdcdc;
  --footer:#6b6b6b;
  --dark-box:#5e5e5e;
}
*{box-sizing:border-box;margin:0;padding:0}
html,body{width:1011px;height:1200px;overflow:hidden}
body{position:relative;background:var(--page);font-family:"PT Sans",sans-serif;color:var(--text)}
.abs{position:absolute}
.site-header{position:absolute;left:0;top:0;width:1011px;height:122px;background:var(--white);box-shadow:0 1px 3px rgba(0,0,0,.08)}
.brand{left:95px;top:10px;width:250px;height:100px;display:flex;align-items:center;gap:10px;padding-left:18px}
.brand-mark{width:28px;height:28px;border-radius:50%;background:var(--gold)}
.brand-name{font-size:24px;font-weight:700;color:#3a3a3a}
.contact-line{right:111px;font-size:15px;color:var(--gold);display:flex;align-items:center;gap:8px}
.contact-line.email{font-size:12.5px}
.nav-rule{left:649px;top:79px;width:252px;height:1px;background:var(--line)}
.main-nav{right:110px;top:92px;display:flex;font-size:11px;color:#555}
.main-nav a{color:inherit;text-decoration:none}
.main-nav .sep{margin:0 20px}
.main-nav .active{color:var(--gold)}
.hero{left:110px;top:143px;width:791px;height:296px;border-radius:3px;background:linear-gradient(180deg,#6f8a4e 0%,#4a4c4a 35%,#3c3d3b 60%,#8c7d62 100%)}
.hero-caption{left:179px;top:219px;width:283px;height:131px;background:rgba(60,60,60,.7);padding:16px 21px;color:var(--white)}
.hero-caption h2{font-size:22px;font-weight:400;line-height:31px}
.hero-caption p{font-size:12px;margin-top:14px}
.slide-arrow{top:275px;width:32px;height:32px}
.welcome h1{left:110px;top:474px;font-size:22px;font-weight:400;color:var(--heading)}
.welcome h1 span{color:var(--gold)}
.welcome p{width:560px;font-size:10.5px;line-height:17px;left:110px}
.promo{left:686px;top:479px;width:215px;height:153px;background:linear-gradient(180deg,#6a6a6a,#555);color:var(--white)}
.promo h3{position:absolute;left:12px;top:12px;font-size:18px;font-weight:400}
.promo .from{position:absolute;left:13px;top:49px;font-size:11px;color:#ddd}
.promo .maker{position:absolute;left:13px;top:67px;font-size:11px;font-weight:700;color:#ddd;letter-spacing:.2px}
.promo .shoes{position:absolute;left:86px;top:52px;width:118px;height:70px;border-radius:8px;background:linear-gradient(90deg,#8a7c68,#4a6a95)}
.promo .pager{position:absolute;left:14px;top:126px;font-size:13px;font-weight:700}
.rule{left:110px;width:791px;height:1px;background:var(--line)}
.section-title{left:110px;top:698px;font-size:22px;font-weight:400;color:var(--gold)}
.pager-dark{left:874px;top:704px;font-size:17px;font-weight:700;color:#555}
.product-photo{top:742px;width:185px;height:103px}
.product-label{top:859px;font-size:14px;color:#555}
.partner-strip{left:110px;top:951px;width:784px;height:102px;background:var(--white);display:flex;align-items:center;justify-content:space-around}
.partner{display:flex;align-items:center;gap:6px;font-size:15px;font-weight:700;color:#444}
.partner i{display:block;width:12px;height:12px;background:#444}
.site-footer{left:0;top:1104px;width:1011px;height:96px;background:linear-gradient(180deg,#6e6e6e,#5a5a5a);color:var(--white)}
.footer-nav{position:absolute;left:110px;top:20px;font-size:12px;display:flex}
.footer-nav .sep{margin:0 13px}
.copyright{position:absolute;left:111px;top:50px;font-size:10.5px}
.social{position:absolute;left:794px;top:27px;display:flex;gap:5px}
.social span{width:23px;height:23px;border-radius:3px}
</style>
</head>
<body>
<header class="site-header">
  <div class="abs brand"><span class="brand-mark"></span><span class="brand-name">TARVIX OIL &amp; GAS</span></div>
  <div class="abs contact-line" style="top:18px">
    <svg width="13" height="13" viewBox="0 0 13 13"><path d="M3 1l2 3-1.3 1.3a7 7 0 003.9 3.9L9 7.9l3 2-1 2C6 12 1 7 1 2z" fill="#888"/></svg>
    (014).728.3901</div>
  <div class="abs contact-line email" style="top:48px">
    <svg width="14" height="10" viewBox="0 0 14 10"><rect x=".5" y=".5" width="13" height="9" fill="none" stroke="#888"/><path d="M.5.5L7 6 13.5.5" fill="none" stroke="#888"/></svg>
    tarvix@harbornet.example</div>
  <div class="abs nav-rule"></div>
  <nav class="abs main-nav">
    <a class="active" href="#">HOME</a><span class="sep">|</span>
    <a href="#">ABOUT US</a><span class="sep">|</span>
    <a href="#">SERVICE</a><span class="sep">|</span>
    <a href="#">PRODUCT</a><span class="sep">|</span>
    <a href="#">CONTACT</a>
  </nav>
</header>

<div class="abs hero" role="img" aria-label="Worker operating a large HDPE pipe fusion machine on a job site"></div>
<div class="abs hero-caption">
  <h2>HDPE pressure pipe &amp; fittings in North America</h2>
  <p>Inquire page for web user to request pricing</p>
</div>
<svg class="abs slide-arrow" style="left:119px" viewBox="0 0 32 32"><circle cx="16" cy="16" r="15.5" fill="#f4f4f4" stroke="#ccc"/><path d="M19 9l-7 7 7 7" fill="none" stroke="#333" stroke-width="3"/></svg>
<svg class="abs slide-arrow" style="left:858px" viewBox="0 0 32 32"><circle cx="16" cy="16" r="15.5" fill="#f4f4f4" stroke="#ccc"/><path d="M13 9l7 7-7 7" fill="none" stroke="#333" stroke-width="3"/></svg>

<section class="welcome">
  <h1 class="abs">Welcome to <span>Tarvix Oil n Gas</span></h1>
  <p class="abs" style="top:516px">Lorem ipsum dolor sit amet, consectetur adipisicing elit, sed do eiusmod tempor incididunt ut labore et dolore magnano aliqua. Ut enim ad minim veniam, quis nostrud exercitation ullamco laboris nisi ut aliquip ex ea commodo consequat.ase Duis aute irure dolor in reprehenderit in voluptate velit esse cillum dolore eu fugiat nulla pariatur. Excepteur sint occaecat cupidatat non proident, sunt in culpa qui officia deserunt mollit anim id est laborum.</p>
  <p class="abs" style="top:602px">Lorem ipsum dolor sit amet, consectetur adipisicing elit, sed do eiusmod tempor incididunt ut labore et dolore magnano aliqua. Ut enim ad minim veniam, quis nostrud exercitation ullamco laboris nisi ut aliquip.</p>
</section>

<aside class="abs promo">
  <h3>Safety Shoes</h3>
  <span class="from">from</span>
  <div class="shoes" role="img" aria-label="Pair of work boots"></div>
  <span class="maker">PELSTRIDE</span>
  <span class="pager">&lt; &gt;</span>
</aside>

<div class="abs rule" style="top:667px"></div>

<h2 class="abs section-title">Our Products</h2>
<span class="abs pager-dark">&lt; &gt;</span>

<div class="abs product-photo" style="left:110px;background:linear-gradient(180deg,#4a5058,#23262b)" role="img" aria-label="Stack of black HDPE pipes"></div>
<div class="abs product-photo" style="left:312px;background:linear-gradient(180deg,#5f8a3a,#9b3a34 50%,#5f8a3a)" role="img" aria-label="Red fusion machine on grass"></div>
<div class="abs product-photo" style="left:514px;background:linear-gradient(180deg,#f2f2f2,#e2e2e2);border:1px solid #ddd" role="img" aria-label="Group of red and grey filters"></div>
<div class="abs product-photo" style="left:716px;background:linear-gradient(90deg,#6b5642,#a88d6e 60%,#c9c9c9)" role="img" aria-label="Worker in uniform and hard hat"></div>

<span class="abs product-label" style="left:110px">HDPE Pipes and Fittings</span>
<span class="abs product-label" style="left:312px">HDPE Fusion Equipment</span>
<span class="abs product-label" style="left:514px">Corlett Strainers</span>
<span class="abs product-label" style="left:716px">Hargrove-Tamsin Uniforms</span>

<div class="abs rule" style="top:915px"></div>

<div class="abs partner-strip">
  <span class="partner"><i style="border-radius:50%"></i>Coastline</span>
  <span class="partner">Velorin Tube</span>
  <span class="partner"><i></i>Fertani</span>
  <span class="partner">Tamsin</span>
  <span class="partner"><i></i>Pelstride</span>
</div>

<footer class="abs site-footer">
  <nav class="footer-nav">
    <span>Home</span><span class="sep">|</span><span>About Us</span><span class="sep">|</span><span>Service</span><span class="sep">|</span><span>Product</span><span class="sep">|</span><span>Contact</span>
  </nav>
  <p class="copyright">(c)2013. Tarvix. All Right Reserved.</p>
  <div class="social">
    <span style="background:#3b5d9c"></span>
    <span style="background:#2aa3d8"></span>
    <span style="background:#1f7fb8"></span>
    <span style="background:#e5742a"></span>
  </div>
</footer>
</body>
</html>
```